fizzy drinks label design

I want to design fizzy drink label for 3 flavors : black grapes, red apple and mojito, band name kestrova, product name TOLMA , product will be in plastic bottle, label size 198 mm X 66mm

```html
<!DOCTYPE html>
<html lang="en">
<head>
<meta charset="utf-8">
<title>TOLMA fizzy drink labels</title>
<link href="https://fonts.googleapis.com/css2?family=Oswald:wght@400;700&family=Varela+Round&family=Source+Sans+3:wght@400;700&display=swap" rel="stylesheet">
<style>
  :root{
    --page:#ffffff;
    --white:#ffffff;
    --brand-red:#e31e24;
    --apple-bg:#000000;
    --apple-accent:#e31e24;
    --grape-bg:#33266b;
    --grape-accent:#7d5cb8;
    --grape-strip:#5a3f9c;
    --mojito-top:#0e9a3e;
    --mojito-bottom:#d4e01c;
    --mojito-accent:#0f6b2e;
    --badge-green:#3aa935;
  }
  html,body{margin:0;padding:0;overflow:hidden}
  body{width:893px;height:1200px;background:var(--page);position:relative}
  .label{position:absolute;left:20px;width:853px;height:284px;display:block}
  .label--apple{top:86px}
  .label--grape{top:458px}
  .label--mojito{top:830px}
  .logo-word{font-family:"Oswald",sans-serif;font-weight:700;fill:var(--brand-red);letter-spacing:2px}
  .tagline{font-family:"Varela Round",sans-serif;fill:var(--white)}
  .maker-word{font-family:"Source Sans 3",sans-serif;font-weight:700;fill:var(--white)}
  .flavor-name{font-family:"Oswald",sans-serif;font-weight:400;fill:var(--white);font-size:17px}
  .net-vol{font-family:"Oswald",sans-serif;fill:var(--white)}
  .facts{font-family:"Source Sans 3",sans-serif;fill:var(--white);font-size:11px}
  .facts-bold{font-weight:700}
  .fine-print{font-family:"Source Sans 3",sans-serif;fill:var(--white);font-size:9px}
  .rule{stroke:var(--white);stroke-width:1}
  .label--mojito .maker-left{fill:var(--mojito-accent)}
</style>
</head>
<body>

<!-- Red apple -->
<svg class="label label--apple" viewBox="0 0 969 323" xmlns="http://www.w3.org/2000/svg">
  <defs>
    <linearGradient id="apple-photo" x1="0" y1="0" x2="1" y2="1"><stop offset="0" stop-color="#f4e6d6"/><stop offset="0.5" stop-color="#c8243a"/><stop offset="1" stop-color="#7a0f1f"/></linearGradient>
  </defs>
  <rect class="panel-bg" width="969" height="323" fill="var(--apple-bg)"/>
  <path class="swoosh" d="M40 323 C60 240 140 180 325 165 C180 185 90 240 65 323Z" fill="var(--apple-accent)"/>
  <path class="swoosh" d="M0 40 C20 25 40 18 62 15 C35 22 15 32 0 48Z" fill="var(--apple-accent)"/>
  <path class="front-edge" d="M310 323 C312 260 318 210 325 185 L325 323Z" fill="var(--apple-accent)"/>
  <text class="flavor-name" transform="translate(30 308) rotate(-90)">RED APPLE</text>
  <text class="logo-word" x="180" y="118" font-size="70" text-anchor="middle">TOLMA</text>
  <text class="tagline" x="185" y="142" font-size="13" text-anchor="middle">Apple based fizzy drink</text>
  <text class="maker-word maker-left" x="212" y="282" font-size="34" text-anchor="middle">kestrova</text>

  <rect x="612" y="21" width="21" height="21" fill="var(--white)"/>
  <rect x="616" y="25" width="13" height="13" fill="var(--badge-green)"/>
  <text class="logo-word" x="490" y="112" font-size="80" text-anchor="middle">TOLMA</text>
  <text class="tagline" x="526" y="134" font-size="14" text-anchor="middle">Apple based fizzy drink</text>
  <circle cx="425" cy="178" r="25" fill="var(--badge-green)" stroke="var(--white)" stroke-width="2"/>
  <rect x="412" y="200" width="198" height="123" rx="40" fill="url(#apple-photo)" role="img" aria-label="Photo of a red apple with a cut half"/>
  <text class="net-vol" x="335" y="290" font-size="9">NET VOL.</text>
  <text class="net-vol" x="335" y="307" font-size="16">250ml</text>
  <text class="flavor-name" transform="translate(633 308) rotate(-90)">RED APPLE</text>

  <text class="maker-word" x="727" y="64" font-size="22" text-anchor="middle">kestrova</text>
  <rect x="673" y="94" width="117" height="98" fill="var(--white)"/>
  <g class="bin-icon" fill="var(--white)"><circle cx="757" cy="208" r="4"/><path d="M752 214h10l4 14h-4l-3-8-3 10h-5z"/><path d="M742 226h16l-2 22h-12z"/></g>
  <g class="facts-table">
    <rect x="800" y="38" width="138" height="212" fill="none" stroke="var(--white)" stroke-width="1.5"/>
    <text class="facts facts-bold" x="805" y="56" font-size="13">Nutritional Facts</text>
    <text class="facts" x="805" y="71">Serving size xxxxx</text>
    <line class="rule" x1="805" y1="78" x2="933" y2="78" stroke-width="2.5"/>
    <text class="facts" x="805" y="95">Amount Per Serving</text>
    <text class="facts facts-bold" x="805" y="114">Calories 120</text>
    <line class="rule" x1="805" y1="121" x2="933" y2="121" stroke-width="2"/>
    <text class="facts" x="929" y="135" text-anchor="end">% Daily Value*</text>
    <line class="rule" x1="805" y1="142" x2="933" y2="142"/>
    <text class="facts" x="805" y="157"><tspan class="facts-bold">Total Fat</tspan> 0g</text>
    <line class="rule" x1="805" y1="164" x2="933" y2="164"/>
    <text class="facts" x="805" y="179"><tspan class="facts-bold">Sodium</tspan> 50mg</text>
    <line class="rule" x1="805" y1="186" x2="933" y2="186"/>
    <text class="facts" x="805" y="201"><tspan class="facts-bold">Sugar</tspan> 30g</text>
    <line class="rule" x1="805" y1="209" x2="933" y2="209"/>
    <text class="facts" x="805" y="224"><tspan class="facts-bold">Protein</tspan> 0g</text>
    <line class="rule" x1="805" y1="231" x2="933" y2="231"/>
    <text class="facts" x="805" y="242" font-size="7">*Sample text</text>
  </g>
  <g class="fine-print">
    <text x="668" y="272">Lorem ipsum dolor sit amet, consectetuer adipiscing elit, sed diam</text>
    <text x="668" y="284">nonummy nibh euismod tincidunt ut laoreet dolore magna aliquam</text>
    <text x="668" y="296">erat Lorem ipsum dolor sit amet, consectetuer adipiscing elit, sed</text>
    <text x="668" y="308">diam nonummy nibh euismod tincidunt ut laoreet dolore magna</text>
  </g>
</svg>

<!-- Black grapes -->
<svg class="label label--grape" viewBox="0 0 969 323" xmlns="http://www.w3.org/2000/svg">
  <defs>
    <radialGradient id="grape-front" cx="0.55" cy="0.4" r="0.7"><stop offset="0" stop-color="#8a76c4"/><stop offset="1" stop-color="#4a3690"/></radialGradient>
    <linearGradient id="grape-photo" x1="0" y1="0" x2="1" y2="1"><stop offset="0" stop-color="#5d8a34"/><stop offset="0.4" stop-color="#2a2440"/><stop offset="1" stop-color="#15121f"/></linearGradient>
  </defs>
  <rect width="969" height="323" fill="var(--grape-bg)"/>
  <rect x="325" width="313" height="323" fill="url(#grape-front)"/>
  <rect x="614" width="24" height="323" fill="var(--grape-strip)"/>
  <rect x="0" y="165" width="22" height="158" fill="var(--grape-strip)"/>
  <path d="M40 323 C60 240 140 180 325 165 C180 185 90 240 65 323Z" fill="var(--grape-accent)"/>
  <path d="M0 40 C20 25 40 18 62 15 C35 22 15 32 0 48Z" fill="var(--grape-accent)"/>
  <text class="flavor-name" transform="translate(30 308) rotate(-90)">BLACK GRAPES</text>
  <text class="logo-word" x="180" y="118" font-size="70" text-anchor="middle">TOLMA</text>
  <text class="tagline" x="185" y="142" font-size="13" text-anchor="middle">Grape based fizzy drink</text>
  <text class="maker-word maker-left" x="212" y="282" font-size="34" text-anchor="middle">kestrova</text>

  <rect x="612" y="21" width="21" height="21" fill="var(--white)"/>
  <rect x="616" y="25" width="13" height="13" fill="var(--badge-green)"/>
  <text class="logo-word" x="490" y="112" font-size="80" text-anchor="middle">TOLMA</text>
  <text class="tagline" x="526" y="134" font-size="12" text-anchor="middle">Black Grape based fizzy drink</text>
  <circle cx="388" cy="208" r="25" fill="var(--badge-green)" stroke="var(--white)" stroke-width="2"/>
  <rect x="420" y="162" width="190" height="161" rx="40" fill="url(#grape-photo)" role="img" aria-label="Photo of a bunch of black grapes with leaves"/>
  <text class="net-vol" x="335" y="290" font-size="9">NET VOL.</text>
  <text class="net-vol" x="335" y="307" font-size="16">250ml</text>
  <text class="flavor-name" transform="translate(633 308) rotate(-90)">BLACK GRAPES</text>

  <text class="maker-word" x="727" y="64" font-size="22" text-anchor="middle">kestrova</text>
  <rect x="673" y="94" width="117" height="98" fill="var(--white)"/>
  <g fill="var(--white)"><circle cx="757" cy="208" r="4"/><path d="M752 214h10l4 14h-4l-3-8-3 10h-5z"/><path d="M742 226h16l-2 22h-12z"/></g>
  <g class="facts-table">
    <rect x="800" y="38" width="138" height="212" fill="none" stroke="var(--white)" stroke-width="1.5"/>
    <text class="facts facts-bold" x="805" y="56" font-size="13">Nutritional Facts</text>
    <text class="facts" x="805" y="71">Serving size xxxxx</text>
    <line class="rule" x1="805" y1="78" x2="933" y2="78" stroke-width="2.5"/>
    <text class="facts" x="805" y="95">Amount Per Serving</text>
    <text class="facts facts-bold" x="805" y="114">Calories 120</text>
    <line class="rule" x1="805" y1="121" x2="933" y2="121" stroke-width="2"/>
    <text class="facts" x="929" y="135" text-anchor="end">% Daily Value*</text>
    <line class="rule" x1="805" y1="142" x2="933" y2="142"/>
    <text class="facts" x="805" y="157"><tspan class="facts-bold">Total Fat</tspan> 0g</text>
    <line class="rule" x1="805" y1="164" x2="933" y2="164"/>
    <text class="facts" x="805" y="179"><tspan class="facts-bold">Sodium</tspan> 50mg</text>
    <line class="rule" x1="805" y1="186" x2="933" y2="186"/>
    <text class="facts" x="805" y="201"><tspan class="facts-bold">Sugar</tspan> 30g</text>
    <line class="rule" x1="805" y1="209" x2="933" y2="209"/>
    <text class="facts" x="805" y="224"><tspan class="facts-bold">Protein</tspan> 0g</text>
    <line class="rule" x1="805" y1="231" x2="933" y2="231"/>
    <text class="facts" x="805" y="242" font-size="7">*Sample text</text>
  </g>
  <g class="fine-print">
    <text x="668" y="272">Lorem ipsum dolor sit amet, consectetuer adipiscing elit, sed diam</text>
    <text x="668" y="284">nonummy nibh euismod tincidunt ut laoreet dolore magna aliquam</text>
    <text x="668" y="296">erat Lorem ipsum dolor sit amet, consectetuer adipiscing elit, sed</text>
    <text x="668" y="308">diam nonummy nibh euismod tincidunt ut laoreet dolore magna</text>
  </g>
</svg>

<!-- Mojito -->
<svg class="label label--mojito" viewBox="0 0 969 323" xmlns="http://www.w3.org/2000/svg">
  <defs>
    <linearGradient id="mojito-bg" x1="0" y1="0" x2="0" y2="1"><stop offset="0" stop-color="var(--mojito-top)"/><stop offset="1" stop-color="var(--mojito-bottom)"/></linearGradient>
    <radialGradient id="mojito-front" cx="0.5" cy="0.65" r="0.7"><stop offset="0" stop-color="#ffffff"/><stop offset="0.5" stop-color="#e6f19a"/><stop offset="1" stop-color="#36a943"/></radialGradient>
    <linearGradient id="mojito-photo" x1="0" y1="0" x2="1" y2="1"><stop offset="0" stop-color="#e4ee8c"/><stop offset="0.5" stop-color="#b9d84a"/><stop offset="1" stop-color="#3c8a2c"/></linearGradient>
  </defs>
  <rect width="969" height="323" fill="url(#mojito-bg)"/>
  <rect x="325" width="313" height="323" fill="url(#mojito-front)"/>
  <rect x="614" width="24" height="323" fill="var(--mojito-accent)"/>
  <rect x="0" y="165" width="22" height="158" fill="var(--mojito-accent)"/>
  <path d="M40 323 C60 240 140 180 325 165 C180 185 90 240 65 323Z" fill="var(--mojito-accent)"/>
  <path d="M0 40 C20 25 40 18 62 15 C35 22 15 32 0 48Z" fill="var(--mojito-accent)"/>
  <path d="M310 323 C312 260 318 210 325 185 L325 323Z" fill="var(--mojito-accent)"/>
  <text class="flavor-name" transform="translate(30 308) rotate(-90)">MOJITO</text>
  <text class="logo-word" x="180" y="118" font-size="70" text-anchor="middle">TOLMA</text>
  <text class="tagline" x="185" y="142" font-size="13" text-anchor="middle">Mojito based fizzy drink</text>
  <text class="maker-word maker-left" x="212" y="282" font-size="34" text-anchor="middle">kestrova</text>

  <rect x="612" y="21" width="21" height="21" fill="var(--white)"/>
  <rect x="616" y="25" width="13" height="13" fill="var(--badge-green)"/>
  <text class="logo-word" x="490" y="112" font-size="80" text-anchor="middle">TOLMA</text>
  <text class="tagline" x="526" y="134" font-size="13" text-anchor="middle">Mojito based fizzy drink</text>
  <circle cx="567" cy="178" r="25" fill="var(--brand-red)" stroke="var(--white)" stroke-width="2"/>
  <rect x="375" y="170" width="215" height="140" rx="50" fill="url(#mojito-photo)" role="img" aria-label="Photo of lime halves with mint leaves"/>
  <text class="net-vol" x="335" y="290" font-size="9" style="fill:var(--mojito-accent)">NET VOL.</text>
  <text class="net-vol" x="335" y="307" font-size="16" style="fill:var(--mojito-accent)">250ml</text>
  <text class="flavor-name" transform="translate(633 308) rotate(-90)">MOJITO</text>

  <text class="maker-word" x="727" y="64" font-size="22" text-anchor="middle">kestrova</text>
  <rect x="673" y="94" width="117" height="98" fill="var(--white)"/>
  <g fill="var(--white)"><circle cx="757" cy="208" r="4"/><path d="M752 214h10l4 14h-4l-3-8-3 10h-5z"/><path d="M742 226h16l-2 22h-12z"/></g>
  <g class="facts-table">
    <rect x="800" y="38" width="138" height="212" fill="none" stroke="var(--white)" stroke-width="1.5"/>
    <text class="facts facts-bold" x="805" y="56" font-size="13">Nutritional Facts</text>
    <text class="facts" x="805" y="71">Serving size xxxxx</text>
    <line class="rule" x1="805" y1="78" x2="933" y2="78" stroke-width="2.5"/>
    <text class="facts" x="805" y="95">Amount Per Serving</text>
    <text class="facts facts-bold" x="805" y="114">Calories 120</text>
    <line class="rule" x1="805" y1="121" x2="933" y2="121" stroke-width="2"/>
    <text class="facts" x="929" y="135" text-anchor="end">% Daily Value*</text>
    <line class="rule" x1="805" y1="142" x2="933" y2="142"/>
    <text class="facts" x="805" y="157"><tspan class="facts-bold">Total Fat</tspan> 0g</text>
    <line class="rule" x1="805" y1="164" x2="933" y2="164"/>
    <text class="facts" x="805" y="179"><tspan class="facts-bold">Sodium</tspan> 50mg</text>
    <line class="rule" x1="805" y1="186" x2="933" y2="186"/>
    <text class="facts" x="805" y="201"><tspan class="facts-bold">Sugar</tspan> 30g</text>
    <line class="rule" x1="805" y1="209" x2="933" y2="209"/>
    <text class="facts" x="805" y="224"><tspan class="facts-bold">Protein</tspan> 0g</text>
    <line class="rule" x1="805" y1="231" x2="933" y2="231"/>
    <text class="facts" x="805" y="242" font-size="7">*Sample text</text>
  </g>
  <g class="fine-print" style="fill:var(--mojito-accent)">
    <text x="668" y="272" style="fill:inherit">Lorem ipsum dolor sit amet, consectetuer adipiscing elit, sed diam</text>
    <text x="668" y="284" style="fill:inherit">nonummy nibh euismod tincidunt ut laoreet dolore magna aliquam</text>
    <text x="668" y="296" style="fill:inherit">erat Lorem ipsum dolor sit amet, consectetuer adipiscing elit, sed</text>
    <text x="668" y="308" style="fill:inherit">diam nonummy nibh euismod tincidunt ut laoreet dolore magna</text>
  </g>
</svg>

</body>
</html>
```